Business card, letterhead, envelope design, email footer for non-profit private equity association
Riviera Growth Capital and Seed Funding Society
Business card, letterhead, envelope design, email footer for non-profit private equity association - Financial Services
Creative Brief
Simple
Tobias Hernquist
Head of Operations
17, Rue des Orangers 98000 Monaco
thernquist@rgsf-example.org
www.rgsf-example.org
Stationery will be prepared for all 7-8 Board Members of our non-profit association. The stationery design is a subsequent process of the new logo design, which has just been created. The Riviera Growth Capital & Seed Funding Society (RGSF) stands for: seriousness and professionalism. Our official website is http://www.rgsf-example.org Please note that this website still includes the OLD logo and layout (to be changed shortly, so please do not let that influence you. This is more to show you the content rather than the design.

```html
<!DOCTYPE html>
<html lang="en">
<head>
<meta charset="utf-8">
<title>RGSF Business Card</title>
<link href="https://fonts.googleapis.com/css2?family=Open+Sans:wght@400;600;700;800&display=swap" rel="stylesheet">
<style>
  :root {
    --charcoal: #3a3a3c;
    --charcoal-deep: #2f2f31;
    --brand-red: #e01f26;
    --paper: #ffffff;
    --ink: #4a4a4a;
    --backdrop: #e4e3e1;
  }
  * { margin: 0; padding: 0; box-sizing: border-box; }
  html, body {
    width: 1200px; height: 909px; overflow: hidden;
    background: var(--backdrop);
    font-family: "Open Sans", Arial, sans-serif;
  }
  .canvas { position: relative; width: 1200px; height: 909px; }
  .card {
    position: absolute; top: 70px;
    width: 440px; height: 770px;
    background: var(--paper);
    overflow: hidden;
    box-shadow: 0 6px 18px rgba(0,0,0,0.18);
  }
  .card--front { left: 130px; }
  .card--back { left: 630px; }
  .card__shape { position: absolute; inset: 0; width: 100%; height: 100%; }

  .brand { position: absolute; left: 44px; }
  .brand__mark { display: flex; align-items: center; gap: 14px; }
  .brand__square { width: 26px; height: 26px; background: var(--brand-red); }
  .brand__name {
    font-weight: 800; font-size: 78px; line-height: 1; letter-spacing: 2px;
  }
  .brand__tagline {
    margin-top: 8px;
    font-weight: 600; font-size: 16.5px; line-height: 1.2;
    text-transform: uppercase; letter-spacing: 0.3px;
  }
  .card--front .brand { top: 92px; }
  .card--front .brand__name,
  .card--front .brand__tagline { color: var(--paper); }
  .card--back .brand { top: 96px; }
  .card--back .brand__name,
  .card--back .brand__tagline { color: var(--charcoal); }

  .contact {
    position: absolute; left: 170px; top: 388px;
    color: var(--ink); font-size: 16px; line-height: 1.45;
  }
  .contact__name { color: var(--brand-red); font-weight: 700; font-size: 19px; }
  .contact__role { font-size: 17px; margin-bottom: 14px; }
  .contact__address { margin-bottom: 6px; }
  .contact__label { color: var(--brand-red); font-weight: 700; }
  .contact__web { margin-top: 2px; }

  .back__web {
    position: absolute; right: 26px; bottom: 40px;
    color: var(--paper); font-size: 12px; letter-spacing: 0.5px;
    writing-mode: vertical-rl; transform: rotate(180deg);
  }
</style>
</head>
<body>
<main class="canvas">

  <section class="card card--front" aria-label="Business card front">
    <svg class="card__shape" viewBox="0 0 440 770" preserveAspectRatio="none" aria-hidden="true">
      <path d="M0 0 H440 V250 C330 260 120 300 0 380 Z" fill="var(--charcoal)"/>
      <path d="M0 380 C120 300 330 260 440 250 V268 C330 278 130 318 0 402 Z" fill="var(--brand-red)"/>
    </svg>
    <div class="brand">
      <div class="brand__mark">
        <span class="brand__name">RGSF</span>
        <span class="brand__square"></span>
      </div>
      <p class="brand__tagline">Riviera Growth Capital and<br>Seed Funding Society</p>
    </div>
    <div class="contact">
      <p class="contact__name">Marin Calloway-Reed</p>
      <p class="contact__role">Consultant</p>
      <p class="contact__address">417 9th floor,<br>Harbour Line<br>Road QZT</p>
      <p><span class="contact__label">Ph:</span> 010 555 0147</p>
      <p><span class="contact__label">Cell:</span> 010 555 0147</p>
      <p><span class="contact__label">Fax:</span> 010 555 0147</p>
      <p><span class="contact__label">Email:</span> yourname@sitename-example.com</p>
      <p class="contact__web">www.yoursite-example.com</p>
    </div>
  </section>

  <section class="card card--back" aria-label="Business card back">
    <svg class="card__shape" viewBox="0 0 440 770" preserveAspectRatio="none" aria-hidden="true">
      <path d="M0 360 C120 300 320 250 440 240 V770 H0 Z" fill="var(--charcoal)"/>
      <path d="M0 342 C120 282 320 232 440 222 V240 C320 250 120 300 0 360 Z" fill="var(--brand-red)"/>
    </svg>
    <div class="brand">
      <div class="brand__mark">
        <span class="brand__name">RGSF</span>
        <span class="brand__square"></span>
      </div>
      <p class="brand__tagline">Riviera Growth Capital and<br>Seed Funding Society</p>
    </div>
    <p class="back__web">www.yoursite-example.com</p>
  </section>

</main>
</body>
</html>
```